BrookVale Collision Repair Web Site

Create a web site that will inform my potential customers about the services I provide. We are a Automotive Collision repair business that uses the latest state of the art equipment, computerized paint matching highly trained technicians, have over 30 years experience. We work with all all insurance programs. Our Moto is "Fixed Right, The First Time, Every Time". BrookVale, The trusted pick in collision repair.

Target Market(s)

People that have been in a auto collision, needs windshield replaced, people that drive 10 year or newer cars

Industry/Entity Type

Automotive

Coding

Coded - Design and coding required

Number of Pages Required

4 page

Font styles to use
Sans Serif

Requirements
Must have
• Logo, Place for Phone number, I need to be able to put the code in so I can use a tracking phone number
• site needs to be mobile ready or adaptive
• May want to have a photo of a high end car
• here is a web site for example with the pages that I want
• https://www.pondlyautobody.example/online-repair-estimate,
• https://www.pondlyautobody.example/schedule-appointment
• https://www.pondlyautobody.example/collision-repair/auto-body-repair
• https://www.pondlyautobody.example/contact
Nice to have
• Be great if the Car in the log could have the front damaged then have it fix in a animation. Not sure if could be done here

```html
<!DOCTYPE html>
<html lang="en">
<head>
<meta charset="utf-8">
<title>BrookVale Collision Repair</title>
<link href="https://fonts.googleapis.com/css2?family=Montserrat:wght@400;500;600;700&display=swap" rel="stylesheet">
<style>
:root{
  --blue:#0b4f9e;
  --blue-dark:#08407f;
  --nav-top:#1a6fd1;
  --nav-bottom:#0a4fa8;
  --btn:#3a97e6;
  --green:#9bd33a;
  --ink:#222;
  --text:#333;
  --white:#fff;
  --footer:#2e2e2e;
  --rule:#c9c9c9;
}
*{box-sizing:border-box;margin:0;padding:0}
html,body{width:737px;height:1200px;overflow:hidden;background:#fff}
body{font-family:"Montserrat",Arial,sans-serif;color:var(--text);position:relative}
.abs{position:absolute}

/* header */
.site-header{left:0;top:0;width:737px;height:63px;background:#fff}
.brand{left:136px;top:22px;font-size:19px;font-weight:700;color:var(--blue);letter-spacing:.3px}
.brand-mark{left:118px;top:25px;width:13px;height:13px;border-radius:50%;background:var(--blue)}
.contact-info{left:462px;top:13px;font-size:6.6px;line-height:9.6px;color:#333}
.social{top:14px;width:18px;height:18px;background:var(--blue);border-radius:2px}
.find-us{left:605px;top:13px;width:33px;height:33px;border:1px solid #999;border-radius:3px;background:#e8e8e8}

/* nav */
.main-nav{left:0;top:63px;width:737px;height:29px;background:linear-gradient(var(--nav-top),var(--nav-bottom))}
.main-nav a{position:absolute;top:10px;font-size:6.8px;font-weight:600;color:var(--white);text-decoration:none}
.main-nav a.active{color:var(--green)}

/* hero */
.hero{left:0;top:92px;width:737px;height:269px;background:linear-gradient(100deg,#d9dfe6 0%,#c9333a 35%,#e24a4f 55%,#efe9e4 75%,#5a5f6a 100%)}
.hero-title{left:24px;top:101px;width:247px;height:42px;background:var(--blue);color:var(--white);font-size:12.2px;font-weight:700;line-height:16px;padding:5px 5px;white-space:nowrap;overflow:hidden}
.hero-point{left:24px;width:247px;background:rgba(255,255,255,.93);font-size:6.3px;line-height:9.2px;padding:4px 9px;color:#333}
.btn{display:block;background:var(--btn);color:var(--white);font-size:6.6px;font-weight:600;text-align:center;text-decoration:none}
.btn-appointment{left:90px;top:307px;width:116px;height:22px;line-height:22px}

/* welcome */
.welcome-title{left:0;top:368px;width:737px;text-align:center;font-size:15px;font-weight:700;color:var(--ink)}
.welcome-text{left:150px;top:390px;width:437px;text-align:center;font-size:6.3px;line-height:9.3px;color:#333}
.rule{left:150px;top:441px;width:438px;height:1px;background:var(--rule)}

/* estimate */
.estimate-title{left:155px;top:460px;font-size:11px;font-weight:600;color:var(--ink)}
.estimate-text{left:155px;top:480px;width:210px;font-size:6.3px;line-height:9.2px;color:#333}
.btn-estimate{left:199px;top:572px;width:116px;height:23px;line-height:23px}

/* safety band */
.safety{left:0;top:605px;width:737px;height:238px;background:var(--blue)}
.safety-title{left:155px;top:617px;font-size:14.5px;font-weight:700;color:var(--white);line-height:17px}
.safety-text{color:var(--white);font-size:6.3px;font-weight:600;line-height:9.3px}
.safety-head{color:var(--green);font-weight:600}

/* faq */
.faq{left:0;top:843px;width:737px;height:284px;background:linear-gradient(90deg,#1d4f93 0%,#284f88 22%,#b7bfc9 45%,#e7eaee 70%,#d9dde3 100%)}
.faq-title{left:357px;top:853px;font-size:11px;font-weight:700;color:var(--ink)}
.faq-q{left:374px;width:214px;background:var(--blue);color:var(--white);font-size:6.3px;font-weight:600;line-height:9.2px;text-align:center;padding:0 7px;display:flex;align-items:center;justify-content:center}

/* reviews & footer */
.reviews{left:0;top:1142px;width:737px;text-align:center;font-size:8px;font-weight:600;color:var(--ink)}
.site-footer{left:0;top:1167px;width:737px;height:33px;background:var(--footer);color:var(--white);font-size:6.3px;font-weight:600;text-align:center;line-height:33px}
</style>
</head>
<body>

<header class="site-header abs">
  <span class="brand-mark abs"></span>
  <div class="brand abs">BrookVale</div>
  <address class="contact-info abs" style="font-style:normal">Call Us: 800-555-5555<br>1234 N. Street Address,<br>STATE. 00000</address>
  <span class="social abs" style="left:552px" aria-label="Social page"></span>
  <span class="social abs" style="left:575px" aria-label="Social page"></span>
  <span class="find-us abs" aria-label="Find us"></span>
</header>

<nav class="main-nav abs">
  <a class="active" style="left:262px" href="#">HOME</a>
  <a style="left:302px" href="#">ABOUT</a>
  <a style="left:344px" href="#">SERVICES
    <svg width="6" height="5" viewBox="0 0 6 5" style="vertical-align:middle"><path d="M1 1.5 3 3.5 5 1.5" stroke="#fff" stroke-width="1.1" fill="none"/></svg></a>
  <a style="left:405px" href="#">FAQS</a>
  <a style="left:442px" href="#">CONTACT</a>
</nav>

<section class="hero abs" role="img" aria-label="Smiling driver in a red car receiving keys from a technician"></section>
<h1 class="hero-title abs">Why is BrookVale the Intelligent<br>Choice in Collision Repair?</h1>
<p class="hero-point abs" style="top:148px;height:28px">We ensure that latest OEM approved procedures are followed during each phase of the repair of your vehicle.</p>
<p class="hero-point abs" style="top:180px;height:16px;padding-top:3px">We have the latest in computerized frame equipment.</p>
<p class="hero-point abs" style="top:199px;height:37px">Our technicians are certified in structural repairs ensuring that your vehicle will be as safe for your family as it was the day it left the factory.</p>
<p class="hero-point abs" style="top:240px;height:24px">Our refinish equipment and trained painters will make sure your finish is back to factory finish maybe even better.</p>
<p class="hero-point abs" style="top:269px;height:28px">Each repair including paint and collision repair comes with a limited lifetime warranty as long as you own the vehicle.</p>
<a class="btn btn-appointment abs" href="#">SCHEDULE AN APPOINTMENT</a>

<h2 class="welcome-title abs">Welcome to our Collision Center</h2>
<p class="welcome-text abs">For over 30 years' vehicle owners and fleet managers have trusted our staff for all their collision repairs. Our Nationwide, Lifetime Guarantee and excellent customer service are just a few of the reasons you want to choose BrookVale. We use the latest computerized frame alignment and paint matching technology. Our professional staff of certified technicians take pride in the work they do and strive to deliver the best possible service. BrookVale "The trusted pick in Collision Repair"</p>
<div class="rule abs"></div>

<h2 class="estimate-title abs">Need an estimate?</h2>
<div class="estimate-text abs">
  <p>Walk in estimates are welcome but we prefer to have you call us and schedule your appointment to have your estimate written. This will make sure you don't have to wait any longer than necessary and it will give us proper time to thoroughly inspect your vehicle.</p>
  <p style="margin-top:9px">Already have an estimate completed by your insurance company? &nbsp;Email us your insurance estimate.</p>
</div>
<a class="btn btn-estimate abs" href="#">ONLINE ESTIMATE</a>

<section class="safety abs"></section>
<h2 class="safety-title abs">Is your car safe<br>to drive?</h2>
<p class="safety-text abs" style="left:155px;top:657px;width:130px">First, we hope that no one was injured in the unfortunate event that led you to search for a collision repair facility and we are glad you found us. Now we want to make sure we can help you mitigate any further loss or property or worse yet physical harm.Your car was just involved in a collision and depending on how severe the accident was it is possible that one or more of the many systems the manufacture of your vehicle has designed into your vehicle are no longer able to protect you if you get into another accident before proper repairs have been made.</p>
<p class="safety-head abs" style="left:304px;top:613px;font-size:7.5px">Some examples of this maybe:</p>
<div class="safety-text abs" style="left:313px;top:633px;width:115px">
  <p>If any airbags have been deployed or your airbag light is on after an impact. Your vehicle is not safe to drive. Please call us or have your car towed straight to our shop. Your vehicle is not safe to drive.</p>
  <p style="margin-top:9px">If any seatbelts no longer retract after an accident. Your vehicle is not safe to drive.</p>
</div>
<p class="safety-head abs" style="left:453px;top:613px;width:135px;font-size:6.3px;line-height:9.3px">Listed below are a few examples of impacts that may have compromised your vehicle's safety devices.</p>
<div class="safety-text abs" style="left:462px;top:650px;width:108px">
  <p>If you had a front or rear impact of a speed greater than 5 miles per hour.</p>
  <p style="margin-top:9px">If your doors don't open properly after a front or rear impact.</p>
  <p style="margin-top:9px">If your window will not roll down after a side impact, the intrusion beam may be compromised and the vehicle may not be safe to drive.</p>
  <p style="margin-top:9px">If you are not sure if your car is safe to drive, please give us a call immediately or get your vehicle in to have it inspected. There is no cost for a visual inspection.</p>
</div>

<section class="faq abs" role="img" aria-label="Mechanic in blue overalls holding a wrench in a repair shop"></section>
<h2 class="faq-title abs">FAQ</h2>
<div class="faq-q abs" style="top:874px;height:32px">Q: I have an insurance estimate already do I need to get more estimates?</div>
<div class="faq-q abs" style="top:913px;height:24px">Q: Can you see all the damage during the estimate?</div>
<div class="faq-q abs" style="top:943px;height:42px">Q: I got in an accident and the person that hit me wants to pay to repair my car without filing an insurance claim. Is this a good idea?</div>
<div class="faq-q abs" style="top:992px;height:42px">Q: My final bill was greater than the estimate. Why can't you write an estimate that will include everything that my car will need for repairs?</div>
<div class="faq-q abs" style="top:1041px;height:32px">Q: Why will you have to blend paint into the panels adjacent to the repairs that need to be done on my vehicle?</div>
<div class="faq-q abs" style="top:1081px;height:32px">Q: Why doesn't the paint on my bumper match the paint on the rest of my vehicle?</div>

<h2 class="reviews abs">Reviews</h2>
<footer class="site-footer abs">Copyright 2016 | BrookVale Collision Repair - All rights reserved</footer>

</body>
</html>
```